Brixel capital

We lend hard money loans for fixer upper homes and new constructions.Easy Financing on Fix Homes

Target Market(s)

People that need loans & money to buy a Home

Industry/Entity Type

Mortgage Lender

Font styles to use
Serif
Sans Serif

Colors
ffffff
9ccb3b

Requirements
Must have
• Catchy, modern, Clean
Nice to have
• Easy to read

```html
<!DOCTYPE html>
<html lang="en">
<head>
<meta charset="utf-8">
<title>Brixel capital — stationery set</title>
<link href="https://fonts.googleapis.com/css2?family=Montserrat:wght@700&family=Open+Sans:wght@400;600&display=swap" rel="stylesheet">
<style>
  :root{
    --green:#9ccb3b;
    --white:#ffffff;
    --ink:#111111;
    --paper-bg:#e9e6df;
    --muted:#555555;
    --faint:#eef2e4;
  }
  *{box-sizing:border-box;margin:0;padding:0}
  html,body{width:1200px;height:900px;overflow:hidden}
  body{background:var(--paper-bg);font-family:"Open Sans",Arial,sans-serif;color:var(--ink);position:relative}
  .piece{position:absolute;box-shadow:0 4px 14px rgba(0,0,0,.15);overflow:hidden}
  .brand{display:flex;align-items:center;gap:10px;font-family:"Montserrat",Arial,sans-serif;font-weight:700;color:var(--green);white-space:nowrap}
  .brand-dot{border-radius:50%;background:var(--green);flex:none}
  .dark{background:var(--ink)}
  .light{background:var(--white)}

  .card-front{left:40px;top:40px;width:340px;height:195px;display:flex;align-items:center;justify-content:center}
  .card-front .brand{font-size:26px}
  .card-front .brand-dot{width:22px;height:22px}

  .card-back{left:40px;top:255px;width:340px;height:195px;padding:34px 28px}
  .card-back .person{font-family:"Montserrat",Arial,sans-serif;font-weight:700;font-size:17px}
  .card-back .role{color:var(--green);font-size:11px;font-weight:600;margin:2px 0 14px}
  .card-back .contact{font-size:10px;line-height:1.7;color:var(--muted)}
  .card-back .contact b{color:var(--green);font-weight:600}
  .card-back .brand{position:absolute;right:24px;top:38px;font-size:14px;gap:8px}
  .card-back .brand-dot{width:11px;height:11px}

  .sleeve{left:40px;top:480px;width:340px;height:340px;display:flex;align-items:center;justify-content:center}
  .sleeve .brand{font-size:34px}
  .sleeve .brand-dot{width:28px;height:28px}

  .env-back{left:410px;top:40px;width:440px;height:220px}
  .env-back .flap{position:absolute;left:0;top:0;width:100%;height:62px;background:var(--ink)}
  .env-back .flap-shade{position:absolute;left:0;top:62px;width:100%;height:22px;background:linear-gradient(#dedede,var(--white))}
  .env-back .brand{position:absolute;left:0;right:0;bottom:44px;justify-content:center;font-size:32px;color:var(--faint)}
  .env-back .brand-dot{width:26px;height:26px;background:var(--faint)}

  .env-front{left:410px;top:280px;width:440px;height:220px}
  .env-front .brand{position:absolute;left:26px;top:24px;font-size:20px}
  .env-front .brand-dot{width:16px;height:16px}
  .env-front .return{position:absolute;left:26px;bottom:40px;font-size:9.5px;line-height:1.5}
  .env-front .return em{font-style:normal;color:var(--green)}
  .band{position:absolute;left:0;bottom:0;width:100%;height:30px}

  .disc{left:460px;top:520px;width:340px;height:340px;border-radius:50%;display:flex;align-items:center;justify-content:center}
  .disc .art{position:absolute;inset:8px;border-radius:50%;border:6px solid var(--green);background:radial-gradient(circle,#d9ecb3,#a9d357)}
  .disc .hole{position:relative;width:76px;height:76px;border-radius:50%;background:#d6d6d6;border:14px solid #eeeeee}

  .letterhead{left:880px;top:40px;width:280px;height:396px}
  .letterhead .topline{position:absolute;left:0;top:0;width:100%;height:6px;background:var(--ink)}
  .letterhead .brand{position:absolute;right:24px;top:28px;font-size:15px;gap:8px}
  .letterhead .brand-dot{width:12px;height:12px}
  .letterhead .watermark{position:absolute;left:0;right:0;top:172px;justify-content:center;font-size:26px;color:var(--faint);gap:8px}
  .letterhead .watermark .brand-dot{width:22px;height:22px;background:var(--faint)}
  .letterhead .footer{position:absolute;left:16px;right:16px;bottom:44px;text-align:center;font-size:8px;line-height:1.6}
  .letterhead .footer strong{color:var(--green);font-weight:600}
  .letterhead .footer em{font-style:normal;color:var(--green)}

  .folder{left:880px;top:456px;width:280px;height:396px;display:flex;align-items:center;justify-content:center}
  .folder .brand{font-size:26px;gap:8px}
  .folder .brand-dot{width:22px;height:22px}
</style>
</head>
<body>

  <section class="piece dark card-front" aria-label="Business card front">
    <div class="brand"><span class="brand-dot"></span>Brixel capital</div>
  </section>

  <section class="piece light card-back" aria-label="Business card back">
    <p class="person">Daniel Reyes</p>
    <p class="role">Director</p>
    <p class="contact"><b>Address:</b> 410 Harbor Lane Suite 12<br><b>Phone:</b> (555) 014 2290<br><b>Email:</b> info@brixelcapital.com<br><b>Website:</b> www.brixelcapitalhome.com</p>
    <div class="brand"><span class="brand-dot"></span>Brixel capital</div>
  </section>

  <section class="piece dark sleeve" aria-label="Disc sleeve">
    <div class="brand"><span class="brand-dot"></span>Brixel capital</div>
  </section>

  <section class="piece light env-back" aria-label="Envelope back">
    <div class="flap"></div>
    <div class="flap-shade"></div>
    <div class="brand"><span class="brand-dot"></span>Brixel capital</div>
  </section>

  <section class="piece light env-front" aria-label="Envelope front">
    <div class="brand"><span class="brand-dot"></span>Brixel capital</div>
    <p class="return"><em>If undelivered, please return to:</em><br>410 Harbor Lane, Suite 12, Ashford, NY 10990<br>27 Cedar Row, Millbrook, NY 10992</p>
    <svg class="band" viewBox="0 0 440 30" preserveAspectRatio="none">
      <polygon points="0,8 440,8 440,14 0,14" fill="#111111"/>
      <polygon points="300,14 440,14 440,30 270,30" fill="#9ccb3b"/>
      <polygon points="0,14 300,14 270,30 0,30" fill="#111111"/>
    </svg>
  </section>

  <section class="piece disc" aria-label="Disc">
    <div class="art" role="img" aria-label="Green leafy tree illustration on the disc face"></div>
    <div class="hole"></div>
  </section>

  <section class="piece light letterhead" aria-label="Letterhead">
    <div class="topline"></div>
    <div class="brand"><span class="brand-dot"></span>Brixel capital</div>
    <div class="brand watermark"><span class="brand-dot"></span>Brixel capital</div>
    <p class="footer"><strong>Brixel CAPITAL</strong><br>410 Harbor Lane, Suite 12, Ashford, NY 10990<br>27 Cedar Row, Millbrook, NY 10992<br><em>Phone:</em> (555) 014-2290 | <em>Website:</em> www.brixelcapitalhome.com</p>
    <svg class="band" viewBox="0 0 280 30" preserveAspectRatio="none">
      <polygon points="0,6 280,6 280,11 0,11" fill="#111111"/>
      <polygon points="160,11 280,11 280,30 130,30" fill="#9ccb3b"/>
    </svg>
  </section>

  <section class="piece dark folder" aria-label="Presentation folder">
    <div class="brand"><span class="brand-dot"></span>Brixel capital</div>
  </section>

</body>
</html>
```